GreenGlider Powerpoint Template Project

Develop a custom .ppt template that effectively communicates the GreenGlider value proposition and can be tailored for our different audiences: retail partnerships, strategic partnerships, institutional funding and end customers. Our studies have shown a massive improvement in putting effectiveness when using the GreenGlider solution for just 3-5 minutes per day. We would like this dramatic result to be front and center of our value proposition. Putting makes up a huge percentage of a golfer's score (over 40%), but it's widely known that the average golfer spends very little time practicing putting. Reasons for this are reported as: "it's boring"; "tedious"; "it's easy, so I don't need to practice as much"; "I'd rather spend my limited time with the full swing". Using the GreenGlider, golfers can vastly improve their putting effectiveness with significantly less time and effort than other practice methods. Our company mantra, "precision practice" is the "how" in our solution, but ROPI - Return on Parctice Investment - is our real value proposition.
Target Market(s)
Golfers age 18 to 75 with low-medium to high disposable income
Industry/Entity Type
Sports and Leisure

```html
<!DOCTYPE html>
<html lang="en">
<head>
<meta charset="utf-8">
<title>GreenGlider Presentation Template</title>
<link href="https://fonts.googleapis.com/css2?family=Montserrat:wght@400;500;600;700;800&family=Oswald:wght@300;400&display=swap" rel="stylesheet">
<style>
:root{
  --red:#e0141e;
  --red-dark:#b8101a;
  --ink:#151515;
  --grey-bg:#cfcfcf;
  --paper:#ffffff;
  --text:#3a3a3a;
  --muted:#e4e4e4;
  --grass:#5f9a34;
  --grass-dark:#3b6e22;
}
*{box-sizing:border-box;margin:0;padding:0}
html,body{width:757px;height:1200px;overflow:hidden}
body{background:var(--grey-bg);font-family:"Montserrat",sans-serif;color:var(--text);position:relative}
.board-title{position:absolute;top:42px;left:0;width:100%;text-align:center;font-weight:500;font-size:16px;letter-spacing:.5px;color:var(--ink)}
.slide{position:absolute;background:var(--paper);overflow:hidden;box-shadow:0 6px 12px rgba(0,0,0,.18)}
.slide-cover{left:143px;top:120px;width:470px;height:264px}
.slide-sm{width:344px;height:194px}
.s1{left:30px;top:544px}.s2{left:386px;top:544px}
.s3{left:30px;top:760px}.s4{left:386px;top:760px}
.s5{left:30px;top:982px}.s6{left:386px;top:982px}
.brand{position:absolute;display:flex;align-items:center;gap:3px;font-weight:700;color:var(--ink);letter-spacing:.3px}
.brand-dot{border:2px solid var(--ink);border-radius:50%;display:inline-block}
.slide-sm .brand{top:16px;right:12px;font-size:6px}
.slide-sm .brand-dot{width:9px;height:9px;border-width:1.5px}
.cover-brand{left:26px;top:86px;font-size:12px}
.cover-brand .brand-dot{width:18px;height:18px;border-width:3px}
.cover-title{position:absolute;left:26px;top:122px;font-family:"Oswald",sans-serif;font-weight:400;font-size:21px;line-height:22px;color:var(--ink)}
.cover-rule{position:absolute;left:26px;top:198px;width:220px;height:1px;background:var(--red)}
.cover-url{position:absolute;left:26px;top:207px;font-size:9px;color:var(--ink)}
.slide-head{position:absolute;left:13px;top:18px;font-size:12px;font-weight:400;color:var(--red);padding-bottom:3px;border-bottom:2px solid var(--ink);padding-right:22px}
.slide-head.wide{padding-right:38px}
.para{font-size:4px;line-height:6px;color:var(--text);text-align:justify}
.footer{position:absolute;left:12px;right:12px;bottom:8px;display:flex;align-items:center;gap:4px;font-size:4px;color:var(--ink)}
.footer-line{flex:1;height:.5px;background:var(--red)}
.page-no{width:7px;height:7px;border-radius:50%;background:var(--red);color:#fff;font-size:3.5px;display:flex;align-items:center;justify-content:center}
.photo{position:absolute}
/* intro */
.intro-photo{left:-30px;top:-40px;width:170px;height:210px;border-radius:50%;background:radial-gradient(circle at 45% 55%,#d2232a 0 22%,transparent 23%),linear-gradient(160deg,#d9d9d9 0 20%,#7fae49 45%,var(--grass-dark) 100%)}
.intro-body{position:absolute;left:171px;top:62px;width:160px}
.intro-body h2{font-size:12px;font-weight:400;color:var(--red);border-bottom:2px solid var(--ink);padding-bottom:3px;margin-bottom:9px}
.intro-body .para+.para{margin-top:6px}
/* what we do */
.wwd-text{position:absolute;left:13px;top:50px;width:136px}
.bullets{list-style:none;margin-top:10px}
.bullets li{font-size:4px;line-height:5.5px;padding:2px 0 2px 5px;border-bottom:.5px solid var(--muted);position:relative}
.bullets li::before{content:"";position:absolute;left:0;top:4px;width:1.5px;height:1.5px;background:var(--ink);border-radius:50%}
.wwd-photo{left:175px;top:26px;width:120px;height:120px;border-radius:50%;border:16px solid var(--ink);background:linear-gradient(180deg,#2f5a25 0 35%,#5e9a3b 60%,#7bb24a)}
/* team */
.member{position:absolute;left:13px;right:12px;display:flex;gap:12px}
.member.m1{top:46px;padding-bottom:8px;border-bottom:.5px solid var(--muted)}
.member.m2{top:118px}
.avatar{flex:0 0 58px;height:58px;border-radius:50%;border:6px solid var(--ink);background:linear-gradient(180deg,#8ab0cf,#c9c4b6 55%,#e06a3a);margin-left:6px;margin-right:30px}
.m2 .avatar{background:linear-gradient(180deg,#7ea3c5,#b7b2a8 55%,#7a7f86)}
.member-name{font-size:5px;font-weight:700;color:var(--ink)}
.member-role{font-size:5px;color:var(--red);margin-bottom:4px}
/* partners */
.badges{position:absolute;left:13px;top:40px;display:flex;gap:4px}
.badge{width:104px;height:64px;display:flex;align-items:center;justify-content:center}
.badge.dark{background:var(--ink)}
.badge.light{background:#fff;border:.5px solid #bbb}
.badge-shape{width:60px;height:20px;border-radius:10px}
.dark .badge-shape.green{background:#27a03a}
.light .badge-shape{background:var(--red);width:40px;border-radius:2px}
.dark .badge-shape.white{background:#fff;height:6px;width:80px}
.partner{position:absolute;top:112px;display:flex;gap:11px}
.partner.p1{left:13px}.partner.p2{left:187px;padding-left:13px;border-left:.5px solid var(--muted)}
.partner-photo{width:73px;height:64px;background:linear-gradient(180deg,#4a4a4a,#cfd6dc 60%,#f1f1f1)}
.p2 .partner-photo{width:54px;background:linear-gradient(160deg,#cfc7b8,#5aa99c 55%,#d26a2a)}
.partner-info{padding-top:6px;font-size:5px}
.partner-info .member-name{font-size:5px}
.partner-info .member-role{font-size:5px;margin-bottom:4px}
.partner-url{font-size:3.6px;color:var(--ink)}
/* growth */
.stat{position:absolute;font-weight:800;letter-spacing:-.5px}
.stat.red{color:var(--red)}.stat.dark{color:var(--ink)}
.bar{position:absolute;height:7px;background:var(--muted)}
.bar i{display:block;height:100%;background:var(--red)}
.bar.rev i{background:var(--ink);margin-left:auto}
.silhouette{position:absolute;top:38px;width:32px;height:76px;border-radius:45% 45% 12% 12%}
.sil-red{left:136px;background:linear-gradient(180deg,var(--red),var(--red-dark))}
.sil-dark{left:176px;background:linear-gradient(180deg,#333,var(--ink))}
.stat-block{position:absolute;top:126px;width:82px}
.stat-block .stat{position:static;font-size:17px;color:var(--red)}
.divider-v{position:absolute;top:128px;width:.5px;height:40px;background:var(--muted)}
/* gain */
.donut{position:absolute;left:10px;top:50px}
.gain-caption{position:absolute;left:13px;top:158px;width:120px;font-size:4px;line-height:5.5px;font-style:italic}
.gain-list{position:absolute;left:138px;top:46px;width:196px;border-left:.5px solid var(--muted)}
.gain-row{display:flex;align-items:center;gap:10px;height:29px;padding:0 6px 0 8px;font-size:4px;line-height:5.5px}
.gain-row.hl{background:var(--red);color:#fff}
.gain-icon{flex:0 0 12px;height:12px}
</style>
</head>
<body>

<h1 class="board-title">POWERPOINT TEMPLATE</h1>

<section class="slide slide-cover">
  <div class="brand cover-brand"><span class="brand-dot"></span>GREENGLIDER</div>
  <h2 class="cover-title">PRESENTATION<br>TITLE GOES HERE</h2>
  <div class="cover-rule"></div>
  <div class="cover-url">www.greenglider.com</div>
  <svg width="470" height="264" viewBox="0 0 470 264" style="position:absolute;left:0;top:0">
    <defs>
      <linearGradient id="coverPhoto" x1="0" y1="0" x2="0" y2="1">
        <stop offset="0" stop-color="#e9e2c9"/>
        <stop offset=".35" stop-color="#9fb56a"/>
        <stop offset=".7" stop-color="#5f9a34"/>
        <stop offset="1" stop-color="#3b6e22"/>
      </linearGradient>
      <linearGradient id="sky" x1="0" y1="0" x2="0" y2="1">
        <stop offset="0" stop-color="#3a6fc4"/>
        <stop offset=".55" stop-color="#c9dcf0"/>
        <stop offset=".6" stop-color="#3b7a2b"/>
        <stop offset="1" stop-color="#8cc152"/>
      </linearGradient>
    </defs>
    <path d="M246,264 C200,140 270,10 400,0 L470,0 L470,264Z" fill="var(--red)"/>
    <path d="M262,264 C225,150 290,30 420,18 L470,20 L470,264Z" fill="var(--ink)"/>
    <path d="M272,264 C240,160 300,44 430,34 L470,40 L470,264Z" fill="#fff"/>
    <path d="M278,264 C250,165 305,52 440,44 L470,48 L470,264Z" fill="url(#coverPhoto)" role="img" aria-label="Photo of a golf ball beside the cup on a sunlit putting green"/>
    <circle cx="292" cy="208" r="38" fill="url(#sky)" stroke="var(--red)" stroke-width="5" role="img" aria-label="Photo of a flagstick on a green under blue sky"/>
  </svg>
</section>

<section class="slide slide-sm s1">
  <div class="photo intro-photo" role="img" aria-label="Photo of a gloved hand placing a red ball on a tee on the grass"></div>
  <div class="brand"><span class="brand-dot"></span>GREENGLIDER</div>
  <div class="intro-body">
    <h2>INTRODUCTION</h2>
    <p class="para">GreenGlider helps golfers build a reliable putting stroke in just a few minutes a day. Short, focused sessions replace long and tedious drills, so practice fits into a busy schedule. Our method turns every putt into measurable feedback, giving players clear targets and steady progress. Putting makes up over forty percent of a golfer's score, yet most players rarely practise it, which leaves easy strokes on the table every single round.</p>
    <p class="para">Precision practice is how we work. Return on practice investment is what we deliver: better scores with far less time and effort.</p>
  </div>
  <div class="footer">www.greenglider.com<span class="footer-line"></span><span class="page-no">01</span></div>
</section>

<section class="slide slide-sm s2">
  <h2 class="slide-head">WHAT WE DO</h2>
  <div class="brand"><span class="brand-dot"></span>GREENGLIDER</div>
  <div class="wwd-text">
    <p class="para">We design compact training tools and guided routines that make putting practice quick, engaging and effective. Three to five minutes a day is enough to see a dramatic change in accuracy and consistency on the green.</p>
    <ul class="bullets">
      <li>Daily routines that take under five minutes and fit any schedule</li>
      <li>Instant feedback on stroke path</li>
      <li>Measured progress tracked session after session for every player</li>
      <li>Drills built for all skill levels</li>
      <li>Proven gains in holed putts per round</li>
    </ul>
  </div>
  <div class="photo wwd-photo" role="img" aria-label="Photo of golfers lining up a putt near the flag"></div>
  <div class="footer">www.greenglider.com<span class="footer-line"></span><span class="page-no">02</span></div>
</section>

<section class="slide slide-sm s3">
  <h2 class="slide-head wide">OUR TEAM</h2>
  <div class="brand"><span class="brand-dot"></span>GREENGLIDER</div>
  <div class="member m1">
    <div class="avatar" role="img" aria-label="Portrait photo of co-founder in a cap"></div>
    <div>
      <div class="member-name">MARCUS BELL</div>
      <div class="member-role">Co-founder</div>
      <p class="para">Marcus spent his career in the insurance industry working for leading firms on claims, law and regulation, compliance, risk management and operations. He is a certified process improvement expert who finds and fixes hidden inefficiencies, and he brings that same discipline of measurement and refinement to how golfers practise their putting every day.</p>
    </div>
  </div>
  <div class="member m2">
    <div class="avatar" role="img" aria-label="Portrait photo of co-founder in a white cap"></div>
    <div>
      <div class="member-name">DANIEL CARVER</div>
      <div class="member-role">Co-founder</div>
      <p class="para">Daniel has been around golf his whole life. His father was head pro at a private course for many years, and Daniel spent his summers working the shop and honing his game. He played on his high school varsity team, then built a long career in sales and marketing with major technology companies before returning to the game he loves.</p>
    </div>
  </div>
  <div class="footer">www.greenglider.com<span class="footer-line"></span><span class="page-no">03</span></div>
</section>

<section class="slide slide-sm s4">
  <h2 class="slide-head wide">OUR PARTNERS</h2>
  <div class="brand"><span class="brand-dot"></span>GREENGLIDER</div>
  <div class="badges">
    <div class="badge dark"><span class="badge-shape green"></span></div>
    <div class="badge light"><span class="badge-shape"></span></div>
    <div class="badge dark"><span class="badge-shape white"></span></div>
  </div>
  <div class="partner p1">
    <div class="partner-photo" role="img" aria-label="Portrait photo of a doctor in a white coat"></div>
    <div class="partner-info">
      <div class="member-name">DR. OWEN HARTLEY</div>
      <div class="member-role">MD</div>
      <div class="partner-url">www.fairwayfitlab.com</div>
    </div>
  </div>
  <div class="partner p2">
    <div class="partner-photo" role="img" aria-label="Photo of a coach with a young golfer in a training studio"></div>
    <div class="partner-info">
      <div class="member-name">PAUL RENNER</div>
      <div class="member-role">FOUNDER</div>
      <div class="partner-url">www.swingstudiopro.com</div>
    </div>
  </div>
  <div class="footer">www.greenglider.com<span class="footer-line"></span><span class="page-no">04</span></div>
</section>

<section class="slide slide-sm s5">
  <h2 class="slide-head wide">OUR GROWTH</h2>
  <div class="brand"><span class="brand-dot"></span>GREENGLIDER</div>
  <div class="stat red" style="left:12px;top:54px;font-size:24px">66%</div>
  <div class="bar" style="left:12px;top:78px;width:102px"><i style="width:57%"></i></div>
  <p class="para" style="position:absolute;left:12px;top:93px;width:102px;text-align:left">More holed putts inside ten feet after four weeks of daily GreenGlider sessions.</p>
  <div class="silhouette sil-red" role="img" aria-label="Red silhouette of a golfer mid swing"></div>
  <div class="silhouette sil-dark" role="img" aria-label="Black silhouette of a golfer finishing a swing"></div>
  <div class="stat dark" style="right:12px;top:54px;font-size:24px">34%</div>
  <div class="bar rev" style="left:222px;top:78px;width:110px"><i style="width:45%"></i></div>
  <p class="para" style="position:absolute;left:222px;top:93px;width:110px;text-align:left">Fewer three-putts per round reported by players in our field study group.</p>
  <div class="stat-block" style="left:12px"><div class="stat">20+</div><p class="para" style="text-align:left">Retail partners stocking our trainer nationwide</p></div>
  <div class="divider-v" style="left:110px"></div>
  <div class="stat-block" style="left:130px"><div class="stat">15%</div><p class="para" style="text-align:left">Average drop in putts per round for users</p></div>
  <div class="divider-v" style="left:212px"></div>
  <div class="stat-block" style="left:232px;width:100px"><div class="stat">32K+</div><p class="para" style="text-align:left">Practice sessions logged by golfers this year</p></div>
  <div class="footer">www.greenglider.com<span class="footer-line"></span><span class="page-no">05</span></div>
</section>

<section class="slide slide-sm s6">
  <h2 class="slide-head wide">RECENT GAIN</h2>
  <div class="brand"><span class="brand-dot"></span>GREENGLIDER</div>
  <svg class="donut" width="96" height="96" viewBox="-48 -48 96 96">
    <g stroke="#fff" stroke-width=".6">
      <path d="M0,-46 A46,46 0 0,1 44.6,-11.2 L0,0Z" fill="#e0141e"/>
      <path d="M44.6,-11.2 A46,46 0 0,1 18.1,42.3 L0,0Z" fill="#f0343c"/>
      <path d="M18.1,42.3 A46,46 0 0,1 -13.4,44 L0,0Z" fill="#e8333a"/>
      <path d="M-13.4,44 A46,46 0 0,1 -30.7,34.2 L0,0Z" fill="#a10d16"/>
      <path d="M-30.7,34.2 A46,46 0 0,1 0,-46 L0,0Z" fill="#c2121b"/>
    </g>
    <circle r="20" fill="#fff"/>
    <ellipse cx="0" cy="9" rx="10" ry="3" fill="var(--ink)"/>
    <line x1="1" y1="8" x2="1" y2="-10" stroke="var(--ink)" stroke-width="1.2"/>
    <path d="M1,-10 L9,-7 L1,-4Z" fill="var(--ink)"/>
    <g fill="#fff" font-family="Montserrat,sans-serif" font-size="5.5" font-weight="700" text-anchor="middle">
      <text x="9" y="-29">21%</text>
      <text x="30" y="2">30%</text>
      <text x="16" y="32">11%</text>
      <text x="-12" y="32">7%</text>
      <text x="-33" y="1">42%</text>
    </g>
  </svg>
  <p class="gain-caption">Share of new revenue by channel over the last twelve months across all markets.</p>
  <div class="gain-list">
    <div class="gain-row">
      <svg class="gain-icon" viewBox="0 0 12 12"><circle cx="6" cy="2" r="1.4" fill="var(--ink)"/><path d="M6,3.5 L5,7 L3,11 M5,7 L7.5,11 M6,4.5 L9,2" stroke="var(--ink)" stroke-width="1.2" fill="none"/></svg>
      <span>End customers now make up the largest share of sales, driven by strong word of mouth and online reviews from golfers.</span>
    </div>
    <div class="gain-row hl">
      <svg class="gain-icon" viewBox="0 0 12 12"><path d="M3,1 H9 V4 A3,3 0 0,1 3,4Z M5,7 H7 V9 H5Z M3.5,10 H8.5 V11.5 H3.5Z" fill="#fff"/></svg>
      <span>Retail partnerships grew steadily with new pro shops and sporting goods stores.</span>
    </div>
    <div class="gain-row">
      <svg class="gain-icon" viewBox="0 0 12 12"><path d="M6,1 L11,4 H1Z M2,5 H3.5 V10 H2Z M5.2,5 H6.8 V10 H5.2Z M8.5,5 H10 V10 H8.5Z M1,10.5 H11 V11.5 H1Z" fill="var(--ink)"/></svg>
      <span>Institutional funding secured to expand research and scale production for new markets in the coming season.</span>
    </div>
    <div class="gain-row hl">
      <svg class="gain-icon" viewBox="0 0 12 12"><rect x="1" y="2" width="10" height="6.5" fill="none" stroke="#fff" stroke-width="1.2"/><path d="M5,8.5 V10.5 H7 V8.5 M3.5,11 H8.5" stroke="#fff" stroke-width="1"/></svg>
      <span>Strategic partners bring our training app to more coaches and academies.</span>
    </div>
  </div>
  <div class="footer">www.greenglider.com<span class="footer-line"></span><span class="page-no">06</span></div>
</section>

</body>
</html>
```